Ridgeline Builders Guild Business card

We are looking for a new business card design with photo included.
Our business is a nonprofit construction contractor membership organization. We offer business education, assist with business setup and licensing, provide safety training, and provide a member directory.
URL: www.ridgelinebuildersguild.org
Color code:
CMYK: 0 cyan, 42 magenta, 100 yellow, 0 black for Print.
Hexidecimal: #FF9900
RGB: R 255; G 153; B 0

```html
<!DOCTYPE html>
<html lang="en">
<head>
<meta charset="utf-8">
<title>Ridgeline Builders Guild – Business Card</title>
<link rel="stylesheet" href="https://fonts.googleapis.com/css2?family=Montserrat:wght@400;500;600;700;800;900&display=swap">
<style>
  :root {
    --orange: #FF9900;
    --charcoal: #3b3a3a;
    --charcoal-light: #454444;
    --stage: #2b2e33;
    --white: #ffffff;
    --cream: #FFE2BD;
    --ink: #2e2e2e;
    --sky: #c9d6df;
  }
  * { box-sizing: border-box; margin: 0; padding: 0; }
  html, body {
    width: 1200px; height: 919px; overflow: hidden;
    background: var(--stage);
    font-family: "Montserrat", sans-serif;
  }
  .card {
    position: absolute; left: 240px;
    width: 720px; height: 411px; overflow: hidden;
    box-shadow: 0 10px 30px rgba(0,0,0,.35);
  }
  /* Back side */
  .card--back { top: 30px; background: var(--orange); }
  .back-url {
    position: absolute; left: 40px; top: 385px;
    transform: rotate(-90deg); transform-origin: 0 0;
    color: var(--white); font-size: 17px; font-weight: 400; letter-spacing: .3px;
  }
  .services {
    position: absolute; right: 44px; top: 42px;
    list-style: none; text-align: right;
  }
  .service {
    font-weight: 900; font-size: 38px; line-height: .95;
    text-transform: uppercase; color: var(--cream); margin-bottom: 10px;
  }
  .service span { display: block; }
  .service span:nth-child(2) { color: var(--white); }

  /* Front side */
  .card--front {
    top: 478px;
    background: linear-gradient(160deg, var(--charcoal-light), var(--charcoal) 60%);
  }
  .portrait-frame { position: absolute; left: 0; top: 0; }
  .brand {
    position: absolute; left: 40px; top: 262px;
    width: 240px; height: 84px; background: var(--white);
    display: flex; align-items: center; gap: 10px; padding: 0 16px;
  }
  .brand-dot { width: 16px; height: 16px; border-radius: 50%; background: var(--orange); flex: none; }
  .brand-name {
    font-weight: 800; font-size: 19px; line-height: 1.05;
    color: var(--ink); text-transform: uppercase;
  }
  .person {
    position: absolute; right: 36px; top: 100px; text-align: right; color: var(--white);
  }
  .person-name { font-weight: 800; font-size: 36px; letter-spacing: .3px; line-height: 1; white-space: nowrap; }
  .person-role { font-weight: 600; font-size: 17px; margin-top: 6px; }
  .divider { width: 190px; height: 1.5px; background: var(--white); margin: 10px 0 14px auto; }
  .contact { font-size: 15px; font-weight: 400; line-height: 1.45; white-space: nowrap; }
  .contact b { font-weight: 600; }
</style>
</head>
<body>

<section class="card card--back" aria-label="Card back">
  <p class="back-url">www.ridgelinebuildersguild.org</p>
  <ul class="services">
    <li class="service"><span>Technical</span><span>Assistance</span></li>
    <li class="service"><span>Safety</span><span>&amp; Compliance</span></li>
    <li class="service"><span>Contractor</span><span>Directory</span></li>
    <li class="service"><span>Contractor</span><span>Education</span></li>
  </ul>
</section>

<section class="card card--front" aria-label="Card front">
  <svg class="portrait-frame" width="720" height="411" viewBox="0 0 720 411">
    <defs>
      <clipPath id="ring-cut">
        <path d="M0 0 H272 V205 H720 V411 H0 Z"/>
      </clipPath>
      <radialGradient id="photo-tone" cx="45%" cy="40%" r="65%">
        <stop offset="0" stop-color="#dfe7ec"/>
        <stop offset=".6" stop-color="var(--sky)"/>
        <stop offset="1" stop-color="#e8763d"/>
      </radialGradient>
    </defs>
    <circle class="accent-ring" cx="212" cy="212" r="150" fill="var(--orange)" clip-path="url(#ring-cut)"/>
    <circle class="portrait" cx="250" cy="195" r="105" fill="url(#photo-tone)"
            role="img" aria-label="Portrait photo of the contractor in a white hard hat and safety vest"/>
  </svg>

  <div class="brand">
    <span class="brand-dot"></span>
    <span class="brand-name">Ridgeline Builders Guild</span>
  </div>

  <div class="person">
    <h1 class="person-name">DANIEL REYES</h1>
    <p class="person-role">construction contractor</p>
    <div class="divider"></div>
    <p class="contact">Email; <b>dreyes@ridgelineguild.org</b></p>
    <p class="contact">Call; <b>(503) 555-0148</b></p>
  </div>
</section>

</body>
</html>
```